Basic Letterhead Design

We need a Letterhead design. Our company is in the financial services industry. We are a small bank who lends money. I have uploaded an example our current letterhead design. We would like a new one.

```html
<!DOCTYPE html>
<html lang="en">
<head>
<meta charset="utf-8">
<title>Letter of Offer – Harwell Capital</title>
<link rel="stylesheet" href="https://fonts.googleapis.com/css2?family=Tinos:wght@400;700&family=Arimo:wght@400&display=swap">
<style>
  :root {
    --forest: #234a38;
    --ink: #111111;
    --paper: #ffffff;
    --backdrop: #ebe6df;
    --rule: #555a58;
    --footer-tab: #4a4a4a;
    --signature-fill: #efefef;
  }
  * { box-sizing: border-box; margin: 0; padding: 0; }
  html, body {
    width: 1200px; height: 1113px; overflow: hidden;
    background: var(--backdrop);
  }
  .letterhead {
    position: absolute; left: 220px; top: 20px;
    width: 759px; height: 1073px;
    background: var(--paper);
    overflow: hidden;
    font-family: "Tinos", "Times New Roman", serif;
    color: var(--ink);
  }
  .side-band {
    position: absolute; left: 0; top: 0; bottom: 0; width: 33px;
    background: var(--forest);
  }
  .brand {
    position: absolute; right: 36px; top: 88px;
    font-family: "Tinos", "Times New Roman", serif;
    font-size: 18px; letter-spacing: 0.04em; text-transform: uppercase;
    color: var(--forest);
  }
  .letter-title {
    position: absolute; left: 92px; top: 208px;
    font-size: 19.5px; line-height: 26px; font-weight: 400;
    text-transform: uppercase;
  }
  .letter-body {
    position: absolute; left: 92px; top: 353px; width: 568px;
    font-size: 14.5px; line-height: 17.5px;
  }
  .confidential { font-weight: 700; margin-bottom: 9px; }
  .letter-date { margin-bottom: 16px; }
  .letter-date sup { font-size: 9px; }
  .attention { margin-bottom: 21px; }
  .subject { margin-bottom: 21px; }
  .purpose { margin-bottom: 14px; }
  .offer-intro { margin-bottom: 12px; }
  .offer-terms { list-style: disc; padding-left: 46px; margin-bottom: 42px; }
  .offer-terms li { margin-bottom: 3px; }
  .closing { margin-bottom: 12px; }
  .signature { display: block; width: 108px; height: 38px; margin: 10px 0 16px; }
  .signatory-name { margin-bottom: 14px; }
  .signatory-role { font-weight: 700; }
  .footer-strip {
    position: absolute; left: 76px; right: 0; top: 1013px; height: 27px;
    border: 1px solid var(--rule); border-right: none;
    border-radius: 14px 0 0 14px;
    font-family: "Arimo", Arial, sans-serif; font-size: 12.5px;
    color: #333;
    display: flex; align-items: center; justify-content: space-between;
    padding: 0 92px 0 15px;
  }
  .footer-strip::after {
    content: ""; position: absolute; right: 0; top: -1px; bottom: -1px; width: 10px;
    background: var(--footer-tab);
  }
</style>
</head>
<body>
  <article class="letterhead">
    <div class="side-band"></div>

    <div class="brand">Harwell Capital</div>

    <h1 class="letter-title">Letter of Offer<br>47 Banksia Rd<br>Marlowe NSW 2240</h1>

    <section class="letter-body">
      <p class="confidential">COMMERCIAL-IN-CONFIDENCE</p>
      <p class="letter-date">Wednesday 23<sup>rd</sup> Feb 2022</p>
      <p class="attention">Att: Owen Pritchard Larkfield Realty Darling Point</p>
      <p class="subject">PROPOSED ACQUISITION: 47 Banksia Rd, Marlowe NSW 2240</p>
      <p class="purpose">The purpose of this letter is to provide an in-principle summary of our proposal between the Landowner (‘the Landowner’) and Harwell Capital Pty Ltd (‘Harwell’) to the terms of Sale of Lot 5 DP612408 located at the aforementioned address.</p>
      <p class="offer-intro">Our offer is in two optional parts, as follows:</p>
      <ul class="offer-terms">
        <li>Purchase Price: $1,600,000</li>
        <li>Terms: 12-month Call Option + 4-month extension</li>
        <li>Deposit: 1% Option fee released upon exchange for 12 months. Plus 1% for a further 4 months if extended. (Total 2%)</li>
      </ul>
      <p class="closing">We look forward to hearing from you.</p>
      <p>Best regards,</p>
      <svg class="signature" role="img" aria-label="Handwritten signature of Daniel Ashby" viewBox="0 0 108 38">
        <rect x="0" y="4" width="108" height="30" rx="4" fill="var(--signature-fill)"/>
      </svg>
      <p class="signatory-name">Daniel Ashby</p>
      <p class="signatory-role">Director<br>Harwell Capital Pty Ltd</p>
    </section>

    <footer class="footer-strip">
      <span>HARWELL CAPITAL PTY LTD</span>
      <span>ACN: 218 503 961</span>
    </footer>
  </article>
</body>
</html>
```